Engineering firm Hero image for new web page

We are building a new webpage and need a Hero image. I have included a screen grab of the landing page showing where the image will be located. The company tag line (Engineering Tomorrow’s Automation) will be overlaid on the image so we need to be sure it works with the overlay.
We service a number of different industries, and we want something that is not overly specific so that if potential customers see something they don't recognize that we don't run them off. I have found several examples of a style that I think will work very well for us.
I want the Hero image to incorporate our competencies: Engineering, Automation, Integration, Robotics, Controls, Optimization.
There will be a follow on project to create a second image in the same theme which will highlight our industries served. Those will be: Food processing, Oil & Gas, Automotive, Aerospace, Medical, Contract Manufacturing. This image will be just below the hero and will be part of the “who we are section”

```html
<!DOCTYPE html>
<html lang="en">
<head>
<meta charset="utf-8">
<title>Hero – Engineering Competencies</title>
<link href="https://fonts.googleapis.com/css2?family=Inter:wght@400&display=swap" rel="stylesheet">
<style>
  :root {
    --night: #0c161d;
    --night-deep: #081016;
    --wine: #3c1520;
    --ember: #c4303a;
    --ember-glow: #ff3b3b;
    --hex-line: rgba(255, 255, 255, 0.16);
    --circuit-line: rgba(255, 255, 255, 0.22);
    --icon-white: #f6eeee;
    --city-dark: #1a1a1f;
    --city-warm: #5a3a2a;
  }
  html, body {
    margin: 0;
    padding: 0;
    width: 1200px;
    height: 621px;
    overflow: hidden;
    background: var(--night);
    font-family: "Inter", sans-serif;
  }
  .hero {
    position: relative;
    width: 1200px;
    height: 621px;
    overflow: hidden;
    background: var(--night);
  }
  .hero-art {
    position: absolute;
    inset: 0;
    width: 1200px;
    height: 621px;
    display: block;
  }
  .hex-frame { fill: rgba(255,255,255,0.025); stroke: var(--hex-line); stroke-width: 1.2; }
  .hex-frame.lit { fill: rgba(255,90,90,0.08); }
  .circuit { fill: none; stroke: var(--circuit-line); stroke-width: 1; }
  .circuit-node { fill: rgba(255,255,255,0.45); }
  .accent { fill: none; stroke: var(--ember-glow); stroke-width: 3; }
  .icon-line { fill: none; stroke: var(--icon-white); stroke-width: 4; stroke-linejoin: round; stroke-linecap: round; }
  .icon-fill { fill: var(--icon-white); }
  .icon-hole { fill: #8a3a40; }
  .glow { filter: url(#soft-glow); }
</style>
</head>
<body>
<main class="hero">
  <svg class="hero-art" viewBox="0 0 1276 660" preserveAspectRatio="none" xmlns="http://www.w3.org/2000/svg">
    <defs>
      <linearGradient id="sky" x1="0" y1="0" x2="1" y2="0">
        <stop offset="0" stop-color="#0b1820"/>
        <stop offset="0.45" stop-color="#161820"/>
        <stop offset="0.75" stop-color="#3a1622"/>
        <stop offset="1" stop-color="#4d1a24"/>
      </linearGradient>
      <linearGradient id="city" x1="0" y1="0" x2="0" y2="1">
        <stop offset="0" stop-color="#2a2224" stop-opacity="0"/>
        <stop offset="0.25" stop-color="#3a2a26" stop-opacity="0.7"/>
        <stop offset="0.55" stop-color="#4a2a26" stop-opacity="0.6"/>
        <stop offset="1" stop-color="#1a1618" stop-opacity="0"/>
      </linearGradient>
      <linearGradient id="left-fade" x1="0" y1="0" x2="1" y2="0">
        <stop offset="0" stop-color="#0a141b" stop-opacity="0.95"/>
        <stop offset="0.35" stop-color="#0a141b" stop-opacity="0.55"/>
        <stop offset="0.6" stop-color="#0a141b" stop-opacity="0"/>
      </linearGradient>
      <radialGradient id="ember-wash" cx="0.78" cy="0.4" r="0.5">
        <stop offset="0" stop-color="#b8323c" stop-opacity="0.45"/>
        <stop offset="1" stop-color="#b8323c" stop-opacity="0"/>
      </radialGradient>
      <radialGradient id="icon-halo" cx="0.5" cy="0.5" r="0.5">
        <stop offset="0" stop-color="#ff4a4a" stop-opacity="0.35"/>
        <stop offset="1" stop-color="#ff4a4a" stop-opacity="0"/>
      </radialGradient>
      <filter id="soft-glow" x="-30%" y="-30%" width="160%" height="160%">
        <feGaussianBlur stdDeviation="4" result="b"/>
        <feMerge><feMergeNode in="b"/><feMergeNode in="SourceGraphic"/></feMerge>
      </filter>
    </defs>

    <!-- backdrop -->
    <rect class="backdrop" width="1276" height="660" fill="url(#sky)"/>
    <rect class="city-view" x="0" y="190" width="1276" height="400" fill="url(#city)"
          role="img" aria-label="Night-time aerial view of a city skyline with warm lights"/>
    <rect width="1276" height="660" fill="url(#ember-wash)"/>
    <rect width="1276" height="660" fill="url(#left-fade)"/>

    <!-- circuit traces -->
    <g class="circuit-traces">
      <path class="circuit" d="M460 38 H650 L700 10 H760"/>
      <path class="circuit" d="M436 70 L560 150 H700"/>
      <path class="circuit" d="M355 97 L520 180 H640"/>
      <path class="circuit" d="M355 365 L600 250 H700"/>
      <path class="circuit" d="M460 425 H640 L700 470"/>
      <path class="circuit" d="M470 465 L560 520 H680"/>
      <path class="circuit" d="M460 595 H620 L700 540"/>
      <path class="circuit" d="M830 40 L900 10 H1276"/>
      <path class="circuit" d="M1080 160 H1276"/>
      <path class="circuit" d="M1080 300 L1150 260 H1276"/>
      <path class="circuit" d="M860 120 H1000 L1060 90"/>
      <circle class="circuit-node" cx="460" cy="38" r="2.5"/>
      <circle class="circuit-node" cx="436" cy="70" r="2.5"/>
      <circle class="circuit-node" cx="355" cy="97" r="2.5"/>
      <circle class="circuit-node" cx="355" cy="365" r="2.5"/>
      <circle class="circuit-node" cx="460" cy="425" r="2.5"/>
      <circle class="circuit-node" cx="470" cy="465" r="2.5"/>
      <circle class="circuit-node" cx="460" cy="595" r="2.5"/>
    </g>

    <!-- hexagon grid -->
    <g class="hex-grid">
      <polygon class="hex-frame lit" points="615,205 687,80 833,80 905,205 833,331 687,331"/>
      <polygon class="hex-frame" points="615,456 687,331 833,331 905,456 833,582 687,582"/>
      <polygon class="hex-frame lit" points="833,80 905,-46 1051,-46 1123,80 1051,205 905,205"/>
      <polygon class="hex-frame lit" points="833,330 905,205 1051,205 1123,330 1051,456 905,456"/>
      <polygon class="hex-frame" points="833,581 905,456 1051,456 1123,581 1051,707 905,707"/>
      <polygon class="hex-frame lit" points="1050,205 1122,80 1268,80 1340,205 1268,331 1122,331"/>
      <polygon class="hex-frame" points="1050,456 1122,331 1268,331 1340,456 1268,582 1122,582"/>
    </g>

    <!-- red corner accents -->
    <path class="accent glow" d="M692 128 L712 92 H758"/>
    <path class="accent glow" d="M808 328 H852 L872 292"/>

    <!-- Engineering: gear with globe -->
    <g class="icon icon-engineering glow">
      <circle cx="782" cy="205" r="95" fill="url(#icon-halo)"/>
      <path class="icon-line" d="
        M772 140 h20 l4 16 l14 6 l14 -9 l14 14 l-9 14 l6 14 l16 4 v20 l-16 4 l-6 14 l9 14 l-14 14 l-14 -9 l-14 6 l-4 16 h-20 l-4 -16 l-14 -6 l-14 9 l-14 -14 l9 -14 l-6 -14 l-16 -4 v-20 l16 -4 l6 -14 l-9 -14 l14 -14 l14 9 l14 -6 z"/>
      <circle class="icon-line" cx="782" cy="205" r="36"/>
      <circle class="icon-line" cx="782" cy="205" r="20"/>
      <ellipse class="icon-line" cx="782" cy="205" rx="9" ry="20"/>
      <path class="icon-line" d="M762 205 h40"/>
    </g>

    <!-- Optimization: twin gears -->
    <g class="icon icon-optimization glow">
      <g transform="translate(962 343)">
        <path class="icon-fill" d="M-8 -42 h16 l3 12 l11 5 l11 -7 l11 11 l-7 11 l5 11 l12 3 v16 l-12 3 l-5 11 l7 11 l-11 11 l-11 -7 l-11 5 l-3 12 h-16 l-3 -12 l-11 -5 l-11 7 l-11 -11 l7 -11 l-5 -11 l-12 -3 v-16 l12 -3 l5 -11 l-7 -11 l11 -11 l11 7 l11 -5 z"/>
        <circle class="icon-hole" r="12"/>
      </g>
      <g transform="translate(1036 313)">
        <path class="icon-fill" d="M-6 -34 h12 l3 10 l9 4 l9 -6 l9 9 l-6 9 l4 9 l10 3 v12 l-10 3 l-4 9 l6 9 l-9 9 l-9 -6 l-9 4 l-3 10 h-12 l-3 -10 l-9 -4 l-9 6 l-9 -9 l6 -9 l-4 -9 l-10 -3 v-12 l10 -3 l4 -9 l-6 -9 l9 -9 l9 6 l9 -4 z"/>
        <circle class="icon-hole" r="9"/>
      </g>
    </g>

    <!-- Controls: chip -->
    <g class="icon icon-controls" opacity="0.9">
      <rect class="icon-line" x="752" y="420" width="62" height="62"/>
      <rect class="icon-line" x="762" y="430" width="42" height="42" stroke-dasharray="4 4" stroke-width="2"/>
      <circle class="icon-line" cx="783" cy="451" r="9" stroke-width="3"/>
      <path class="icon-line" stroke-width="2.5" d="
        M762 420 v-24 M772 420 v-30 M783 420 v-36 M794 420 v-30 M804 420 v-24
        M762 482 v24 M772 482 v30 M783 482 v36 M794 482 v30 M804 482 v24
        M752 430 h-24 M752 441 h-30 M752 451 h-34 M752 462 h-30 M752 472 h-24
        M814 430 h24 M814 441 h30 M814 451 h34 M814 462 h30 M814 472 h24"/>
    </g>

    <!-- Robotics and integration placeholders -->
    <rect class="icon-placeholder" x="928" y="25" width="132" height="130" rx="10" fill="rgba(255,255,255,0.08)"
          role="img" aria-label="Line icon of a robotic arm beside a dispensing machine"/>
    <rect class="icon-placeholder" x="1145" y="150" width="120" height="118" rx="10" fill="rgba(255,255,255,0.10)"
          role="img" aria-label="Line icon of an industrial robotic welding arm"/>
    <rect class="icon-placeholder" x="1145" y="372" width="120" height="146" rx="10" fill="rgba(255,255,255,0.09)"
          role="img" aria-label="Line icon of a plant sprouting circuit traces"/>
    <rect class="icon-placeholder" x="940" y="510" width="130" height="120" rx="10" fill="rgba(255,255,255,0.05)"
          role="img" aria-label="Faded icon of a strawberry with a DNA strand and scissors"/>

    <!-- bottom fade -->
    <rect y="560" width="1276" height="100" fill="url(#left-fade)" opacity="0.4"/>
  </svg>
</main>
</body>
</html>
```